this is a new company aimed at the automotive glass industry
what we do is repair cracked windscreens its based in western austraila
I like the old dragracing signwritting logos
I want it to stand out thats why ive gone with the name and title
I dont have a logo but if you can think of one that would be great
but not essential
on the back of the business card i would like Quicker Cheaper Better

Reason: More time needed to decide some great designs Have come through on the eleventh

Target Market(s)

automotive (car yards ,car auctions , trucking companys ect )

Industry/Entity Type

Automotive

Contact Information for Business Card

Pane Stoppers ,
Glass Crack repair specialists ,
Dorian Pelletier ,0437 612 084 ,dpelletier@panestopperswa.com.au

```html
<!DOCTYPE html>
<html lang="en">
<head>
<meta charset="utf-8">
<title>Pane Stoppers – Business Card</title>
<link rel="stylesheet" href="https://fonts.googleapis.com/css2?family=Cinzel:wght@400;700;900&display=swap">
<style>
  :root {
    --page-bg: #e9ebee;
    --card-white: #ffffff;
    --brand-blue: #1fa3e4;
    --brand-blue-light: #7fd0f5;
    --brand-blue-deep: #0b86c9;
    --charcoal: #3a3a3a;
    --text-grey: #4a4a4a;
    --rule-grey: #8a8a8a;
  }
  * { box-sizing: border-box; margin: 0; padding: 0; }
  html, body { width: 1200px; height: 900px; overflow: hidden; }
  body {
    background: var(--page-bg);
    font-family: "Cinzel", serif;
    position: relative;
  }
  .business-card {
    position: absolute;
    left: 75px; top: 150px;
    width: 1050px; height: 600px;
    border-radius: 48px;
    background: var(--card-white);
    overflow: hidden;
    box-shadow: 0 10px 30px rgba(0,0,0,0.15);
  }
  .card-shapes { position: absolute; inset: 0; }
  .brand-name {
    position: absolute;
    left: 0; right: 0; top: 128px;
    text-align: center;
    padding-left: 90px;
    font-weight: 900;
    font-size: 78px;
    letter-spacing: 1px;
    color: var(--brand-blue);
    line-height: 1;
  }
  .tagline {
    position: absolute;
    left: 300px; width: 560px; top: 222px;
    border-top: 2px solid var(--rule-grey);
    border-bottom: 2px solid var(--rule-grey);
    padding: 6px 0;
    text-align: center;
    font-size: 20px;
    letter-spacing: 4px;
    color: var(--text-grey);
  }
  .holder {
    position: absolute;
    right: 570px; top: 310px;
    text-align: right;
    color: var(--text-grey);
    font-size: 23px;
    line-height: 1.45;
  }
  .holder-name { color: var(--brand-blue); font-size: 27px; }
  .divider {
    position: absolute;
    left: 500px; top: 310px;
    width: 2px; height: 180px;
    background: var(--rule-grey);
  }
  .contact-list {
    position: absolute;
    left: 518px; top: 312px;
    list-style: none;
    color: var(--text-grey);
    font-size: 21px;
  }
  .contact-item {
    display: flex; align-items: center;
    height: 36px;
  }
  .contact-icon { width: 22px; height: 22px; margin-right: 12px; flex: none; }
</style>
</head>
<body>
  <div class="business-card">
    <svg class="card-shapes" viewBox="0 0 1050 600" width="1050" height="600" aria-hidden="true">
      <defs>
        <linearGradient id="blueSweep" x1="0" y1="0" x2="1" y2="1">
          <stop offset="0" stop-color="var(--brand-blue-light)"/>
          <stop offset="0.6" stop-color="var(--brand-blue)"/>
          <stop offset="1" stop-color="var(--brand-blue-deep)"/>
        </linearGradient>
        <linearGradient id="baseSweep" x1="0" y1="0" x2="1" y2="0">
          <stop offset="0" stop-color="var(--brand-blue-light)"/>
          <stop offset="1" stop-color="var(--brand-blue)"/>
        </linearGradient>
      </defs>
      <path class="side-sweep" d="M0 0 H125 C45 170 45 420 250 600 H0 Z" fill="url(#blueSweep)"/>
      <path class="side-arc" d="M150 8 C70 190 80 430 300 600 H278 C95 440 85 200 150 8 Z" fill="var(--charcoal)"/>
      <path class="base-sweep" d="M520 600 C760 575 940 565 1050 515 V600 Z" fill="url(#baseSweep)"/>
    </svg>

    <div class="brand-name">PANE STOPPERS</div>
    <div class="tagline">Glass Crack repair specialists</div>

    <div class="holder">
      <div class="holder-name">Dorian Pelletier</div>
      <div class="holder-title">Owner / C.E.O</div>
      <div class="holder-address">Suite # 14, Kembla Bldg,<br>WA 6155</div>
    </div>

    <div class="divider"></div>

    <ul class="contact-list">
      <li class="contact-item">
        <svg class="contact-icon" viewBox="0 0 22 22"><circle cx="11" cy="11" r="11" fill="var(--brand-blue)"/><path d="M7 6 L9 6 L10 9 L8.6 10 C9.3 11.6 10.4 12.7 12 13.4 L13 12 L16 13 L16 15 C16 15.6 15.5 16 15 16 C10 15.7 6.3 12 6 7 C6 6.5 6.4 6 7 6 Z" fill="#fff"/></svg>
        0437 612 084
      </li>
      <li class="contact-item">
        <svg class="contact-icon" viewBox="0 0 22 22"><circle cx="11" cy="11" r="11" fill="var(--brand-blue)"/><rect x="7.5" y="4.5" width="7" height="13" rx="1.3" fill="#fff"/><rect x="8.7" y="6.3" width="4.6" height="7.5" fill="var(--brand-blue)"/></svg>
        0438 205 771
      </li>
      <li class="contact-item">
        <svg class="contact-icon" viewBox="0 0 22 22"><circle cx="11" cy="11" r="11" fill="var(--brand-blue)"/><rect x="6" y="9" width="10" height="7" rx="1" fill="#fff"/><rect x="8" y="5" width="6" height="4" fill="#fff"/></svg>
        0439 318 562
      </li>
      <li class="contact-item">
        <svg class="contact-icon" viewBox="0 0 22 22"><circle cx="11" cy="11" r="11" fill="var(--brand-blue)"/><rect x="5.5" y="7" width="11" height="8" rx="1" fill="#fff"/><path d="M5.8 7.4 L11 11.5 L16.2 7.4" stroke="var(--brand-blue)" stroke-width="1.2" fill="none"/></svg>
        dpelletier@panestopperswa.com.au
      </li>
      <li class="contact-item">
        <svg class="contact-icon" viewBox="0 0 22 22"><circle cx="11" cy="11" r="11" fill="var(--brand-blue)"/><circle cx="11" cy="11" r="5.5" stroke="#fff" stroke-width="1.3" fill="none"/><ellipse cx="11" cy="11" rx="2.3" ry="5.5" stroke="#fff" stroke-width="1.1" fill="none"/><line x1="5.5" y1="11" x2="16.5" y2="11" stroke="#fff" stroke-width="1.1"/></svg>
        www.panestopperswa.com.au
      </li>
    </ul>
  </div>
</body>
</html>
```